Chorefinch/Jobwillow Style Site Design

I need a website similar to jobwillow or chorefinch, the marketing target is for Australian people. Please play with these 2 sites first if you are serious about the project.
I don't have very specific requirement, the functionalities should be like the reference site, but with different & unique design. What I want is a clean, elegant user interface with web2.0 modern style, especially homepage (When I implement your design into actual website, there will be much jquery & ajax modern technique used.)
I need design for the following pages:
1. homepage
2. login page
3. Sign up page
4. browse task page
5. post a task & confirmation page
6. Payment page
7. User Dashboard page
8. Single task page
The features must have photos of friendly looking helpers.
You can also check http://www.beta.errandmoth.example/ for reference. Be as creative & freshness as much as you can!
Target Market(s)
Australian people aging from 15 - 70.
Industry/Entity Type
Marketing
Look and feel
Each slider illustrates characteristics of the customer's brand and the style your logo design should communicate.

```html
<!DOCTYPE html>
<html lang="en">
<head>
<meta charset="utf-8">
<title>Taskperch – Single Task</title>
<link href="https://fonts.googleapis.com/css2?family=PT+Sans:ital,wght@0,400;0,700;1,400&display=swap" rel="stylesheet">
<style>
:root{
  --blue:#2a8db3;
  --blue-dark:#1a6f92;
  --teal-text:#2487ad;
  --orange:#e49a05;
  --orange-dark:#c98300;
  --text:#333;
  --muted:#888;
  --line:#dcdcdc;
  --page:#ececec;
  --footer:#3b3b3b;
  --pale-blue:#d6e9f0;
}
*{box-sizing:border-box;margin:0;padding:0}
html,body{width:1200px;height:1046px;overflow:hidden}
body{font-family:"PT Sans",sans-serif;color:var(--text);background:var(--page);position:relative}
.abs{position:absolute}
a{color:inherit;text-decoration:none}

/* header */
.site-header{position:absolute;left:0;top:0;width:1200px;height:93px;background:#fff;border-top:3px solid var(--blue);box-shadow:0 1px 3px rgba(0,0,0,.08)}
.account-btn{position:absolute;top:-3px;height:23px;background:linear-gradient(#3a9dc2,var(--blue-dark));color:#fff;font-size:10px;text-align:center;line-height:23px;border-radius:0 0 4px 4px}
.logo{position:absolute;left:190px;top:36px;font-size:34px;font-weight:700;font-style:italic;color:var(--blue);letter-spacing:-.5px}
.newsletter-btn{position:absolute;left:382px;top:37px;width:174px;height:39px;border-radius:4px;background:linear-gradient(#4fb0d2,var(--blue-dark));color:#fff;font-size:16px;text-align:center;line-height:39px;box-shadow:0 1px 2px rgba(0,0,0,.3)}
.main-nav a{position:absolute;top:54px;font-size:11px;color:#555;transform:translateX(-50%);white-space:nowrap}
.nav-sep{position:absolute;top:48px;width:1px;height:26px;background:var(--line)}

/* page */
.page-panel{position:absolute;left:180px;top:117px;width:840px;height:815px;background:#fff;border-radius:3px}
.price-box{position:absolute;left:193px;top:131px;width:219px;height:147px;background:linear-gradient(#2d92ba,#7fc0d8 70%,#fff);color:#fff;text-align:center;border-radius:2px}
.price-box .amount{margin-top:10px;font-size:28px}
.price-box .amount span{font-size:13px}
.price-box p{font-size:10px;line-height:18px}
.btn-orange{display:block;background:linear-gradient(#f5b420,var(--orange-dark));color:#fff;text-align:center;border-radius:3px}
.make-offer{position:absolute;left:218px;top:239px;width:168px;height:28px;font-size:15px;line-height:28px}
.whats-this{position:absolute;left:350px;top:277px;font-size:7px;color:var(--orange)}

.discuss-box{position:absolute;left:193px;top:302px;width:219px;height:191px;border:1px solid var(--line);border-radius:3px;background:#fff}
.section-title{color:var(--teal-text);font-size:12px;text-transform:uppercase}
.thumb{background:linear-gradient(135deg,#5b86a6,#c49a7c 55%,#e7ecef);border:1px solid #ccc}
.scrollbar{position:absolute;left:385px;top:342px;width:12px;height:45px;border:1px solid #ccc;background:#f4f4f4}
.scrollbar i{position:absolute;left:1px;top:12px;width:8px;height:14px;border:1px solid #aaa;background:#fff}
.comment-area{position:absolute;left:208px;top:392px;width:190px;height:89px;background:var(--pale-blue)}
.comment-input{position:absolute;left:8px;top:6px;width:173px;height:50px;background:#fff;font-size:8.5px;color:var(--muted);padding:7px 11px;line-height:16px}
.post-btn{position:absolute;left:131px;top:64px;width:49px;height:18px;font-size:8.5px;line-height:18px}

/* task */
.task-title{position:absolute;left:435px;top:141px;font-size:16px;color:var(--teal-text)}
.task-box{position:absolute;left:435px;top:175px;width:569px;height:739px;border:1px solid var(--line);border-radius:2px}
.divider{position:absolute;left:455px;width:527px;height:1px;background:var(--line)}
.meta{position:absolute;font-size:9px;color:var(--orange);display:flex;align-items:center;gap:4px;white-space:nowrap}
.meta svg{width:9px;height:9px}
.btn-blue{position:absolute;background:linear-gradient(#3a9dc2,var(--blue-dark));color:#fff;text-align:center;border-radius:3px}
.task-body{position:absolute;left:458px;width:522px;font-size:8.6px;line-height:15.4px;color:#333}
.label{color:var(--orange)}
.value{color:var(--teal-text)}
.share-btn{position:absolute;top:669px;height:16px;border:1px solid #a9c4d8;background:linear-gradient(#fff,#e8eef4);font-size:9px;color:#2c4e7a;display:flex;align-items:center;gap:3px;padding:0 4px;border-radius:2px}
.share-btn b{width:9px;height:9px;background:#5d7fa8;display:inline-block}
.share-count{position:absolute;top:669px;height:16px;border:1px solid #bbb;background:#fff;font-size:9px;text-align:center;line-height:14px}
.similar-title{position:absolute;left:458px;top:721px;font-size:13px;color:var(--teal-text)}
.similar-item .name{position:absolute;left:511px;font-size:8.6px;color:var(--teal-text)}

/* footer */
.site-footer{position:absolute;left:0;top:949px;width:1200px;height:97px;background:var(--footer)}
.foot-link{position:absolute;top:979px;font-size:7.5px;color:#ddd}
.foot-sep{position:absolute;top:978px;width:1px;height:9px;background:#aaa}
.foot-legal{position:absolute;top:1000px;font-size:7.5px;color:#ddd}
.friend-box{position:absolute;left:620px;top:966px;width:211px;height:58px;background:#fff;border-radius:2px}
.friend-box .smile{position:absolute;left:16px;top:13px;width:32px;height:32px;border-radius:50%;background:radial-gradient(#ffd54a,#f0a500)}
.friend-box h3{position:absolute;left:78px;top:4px;font-size:15px;color:var(--blue);font-weight:700}
.friend-box p{position:absolute;left:78px;top:27px;font-size:7px;color:#555}
.friend-box .invite{position:absolute;left:78px;top:41px;font-size:7px;color:var(--orange);font-weight:700}
.social{position:absolute;top:982px;width:26px;height:26px;border-radius:50%;background:#6a6a6a}
</style>
</head>
<body>

<header class="site-header">
  <a class="account-btn" style="left:896px;width:61px">LOGIN</a>
  <a class="account-btn" style="left:960px;width:59px">SIGNUP</a>
  <div class="logo">Taskperch</div>
  <a class="newsletter-btn">SIGNUP NEWSLETTER</a>
  <nav class="main-nav">
    <a style="left:612px">BROWSE TASKS</a>
    <a style="left:743px">BECOME A RUNNER</a>
    <a style="left:869px">POST A TASK</a>
    <a style="left:986px">HOW IT WORKS</a>
  </nav>
  <span class="nav-sep" style="left:671px"></span>
  <span class="nav-sep" style="left:815px"></span>
  <span class="nav-sep" style="left:926px"></span>
</header>

<main>
  <div class="page-panel"></div>

  <aside>
    <section class="price-box">
      <div class="amount">$ 15 <span>PAID IN CASH</span></div>
      <p style="margin-top:4px">READY TO RUN THIS TASK?<br>MAKE AN OFFER OR COMMENT ON<br>THIS TASK BELOW.</p>
    </section>
    <a class="btn-orange make-offer">MAKE OFFER</a>
    <a class="whats-this">WHAT'S THIS?</a>

    <section class="discuss-box">
      <h2 class="section-title abs" style="left:14px;top:11px">Discuss this task</h2>
      <div class="abs" style="left:14px;top:31px;width:190px;height:1px;background:var(--line)"></div>
    </section>
    <div class="thumb abs" role="img" aria-label="Profile photo of Ed C." style="left:208px;top:345px;width:41px;height:35px"></div>
    <div class="abs" style="left:260px;top:348px;font-size:8.5px;color:var(--teal-text)">ED C. <span style="color:var(--muted);font-size:7.5px">POSTED THIS TASK</span></div>
    <div class="abs" style="left:260px;top:362px;font-size:8.5px;font-style:italic;color:var(--teal-text)">55 mins ago</div>
    <div class="scrollbar"><i></i></div>
    <div class="comment-area">
      <div class="comment-input">Ask a comment, leave a question or introduce yourself here</div>
      <a class="btn-orange post-btn">POST</a>
    </div>
  </aside>

  <h1 class="task-title">WRITE 5 ONLINE STORE REVIEWS AND 1 PROFILE IMAGE</h1>
  <div class="task-box"></div>

  <div class="thumb abs" role="img" aria-label="Photo of the task poster" style="left:456px;top:195px;width:102px;height:91px;border:3px solid #fff;outline:1px solid #ddd"></div>
  <div class="abs" style="left:575px;top:199px;font-size:10px">Posted by <span style="color:var(--orange)">Ed C.</span></div>
  <div class="abs" style="left:575px;top:216px;font-size:10px">9 minutes ago</div>
  <div class="meta" style="left:574px;top:240px">
    <svg viewBox="0 0 10 10"><path d="M5 0a3.5 3.5 0 0 0-3.5 3.5C1.5 6 5 10 5 10s3.5-4 3.5-6.5A3.5 3.5 0 0 0 5 0z" fill="#2a8db3"/><circle cx="5" cy="3.5" r="1.3" fill="#fff"/></svg>Online/Phone
    <svg viewBox="0 0 10 10" style="margin-left:8px"><circle cx="5" cy="5" r="4" fill="none" stroke="#2a8db3" stroke-width="1.4"/><path d="M5 2.5V5h2" stroke="#2a8db3" fill="none" stroke-width="1.2"/></svg>Due in 8 days
    <svg viewBox="0 0 10 10" style="margin-left:8px"><rect x="0" y="2" width="7" height="7" fill="#7bb8d4"/><rect x="3" y="0" width="7" height="7" fill="#2a8db3"/></svg>Copy Task
  </div>
  <a class="btn-blue" style="left:575px;top:262px;width:83px;height:20px;font-size:9px;line-height:20px">Open to Offers</a>
  <div class="divider" style="top:303px"></div>

  <div class="task-body" style="top:320px">Lorem Ipsum is simply dummy text of the printing and typesetting industry. Lorem Ipsum has been the industry's standard dummy text ever since the 1500s, when an unknown printer took a galley of type and scrambled it to make a type specimen book. It has survived not only five centuries, but also the leap into electronic typesetting, remaining essentially unchanged. It was popularised in the 1960s with the release of Lettergrid sheets containing Lorem Ipsum passages, and more recently with desktop publishing software like Pagesetter Pro including versions of Lorem Ipsum.Lorem Ipsum is simply dummy text of the printing and typesetting industry. Lorem Ipsum has been the industry's standard dummy text ever since the 1500s, when an unknown printer took a galley of type and scrambled it to make a type specimen book. It has survived not only five centuries, but also the leap into electronic typesetting, remaining essentially unchanged. It was popularised in the 1960s with the release of Lettergrid sheets containing Lorem Ipsum passages, and more recently with desktop publishing software like Pagesetter Pro including versions of Lorem Ipsum.</div>
  <div class="task-body" style="top:474px">Lorem Ipsum is simply dummy text of the printing and typesetting industry. Lorem Ipsum has been the industry's standard dummy text ever since the 1500s, when an unknown printer took a galley of type and scrambled it to make a type specimen book. It has survived not only five centuries, but also the leap into electronic typesetting, remaining essentially unchanged. It was popularised in the 1960s with the release of Lettergrid sheets containing Lorem Ipsum passages, and more recently with desktop publishing software like Pagesetter Pro including versions of Lorem Ipsum.</div>
  <div class="abs" style="left:459px;top:564px;font-size:10.5px">Cheers</div>
  <div class="abs" style="left:459px;top:579px;font-size:10.5px;color:var(--orange)">Ed</div>
  <div class="divider" style="top:603px"></div>

  <div class="abs" style="left:459px;top:620px;font-size:10px"><span class="label">Category</span></div>
  <div class="abs" style="left:513px;top:620px;font-size:10px" class="label"><span class="label">|</span></div>
  <div class="abs value" style="left:529px;top:620px;font-size:10px">Surveys/Mystery Shopping</div>
  <div class="abs label" style="left:459px;top:640px;font-size:10px">Due by</div>
  <div class="abs label" style="left:513px;top:640px;font-size:10px">|</div>
  <div class="abs value" style="left:529px;top:640px;font-size:10px">02 May 2013</div>
  <a class="btn-blue" style="left:814px;top:632px;width:168px;height:19px;font-size:9.5px;line-height:19px">Report this task as inappropriate</a>
  <div class="abs label" style="left:459px;top:672px;font-size:10px">Share</div>
  <a class="share-btn" style="left:494px"><b></b>Post</a>
  <div class="share-count" style="left:546px;width:31px">7</div>
  <a class="share-btn" style="left:585px"><b></b>Like</a>
  <div class="share-count" style="left:630px;width:19px">3</div>
  <div class="divider" style="top:705px"></div>

  <h2 class="similar-title">SIMILAR TASKS</h2>
  <section class="similar-list">
    <div class="similar-item">
      <div class="thumb abs" role="img" aria-label="Task poster photo" style="left:460px;top:749px;width:41px;height:35px"></div>
      <div class="name" style="top:752px">WRITE 5 ONLINE STORE REVIEWS AND 1 PROFILE IMAGE</div>
      <div class="meta" style="left:511px;top:770px"><svg viewBox="0 0 10 10"><path d="M5 0a3.5 3.5 0 0 0-3.5 3.5C1.5 6 5 10 5 10s3.5-4 3.5-6.5A3.5 3.5 0 0 0 5 0z" fill="#2a8db3"/></svg>Online/Phone<svg viewBox="0 0 10 10" style="margin-left:8px"><circle cx="5" cy="5" r="4" fill="none" stroke="#2a8db3" stroke-width="1.4"/></svg>Due in 8 days<b style="color:var(--blue);margin-left:12px">$</b>$ 15</div>
    </div>
    <div class="similar-item">
      <div class="thumb abs" role="img" aria-label="Task poster photo" style="left:460px;top:804px;width:41px;height:35px"></div>
      <div class="name" style="top:807px">WRITE 5 ONLINE STORE REVIEWS AND 1 PROFILE IMAGE</div>
      <div class="meta" style="left:511px;top:825px"><svg viewBox="0 0 10 10"><path d="M5 0a3.5 3.5 0 0 0-3.5 3.5C1.5 6 5 10 5 10s3.5-4 3.5-6.5A3.5 3.5 0 0 0 5 0z" fill="#2a8db3"/></svg>Online/Phone<svg viewBox="0 0 10 10" style="margin-left:8px"><circle cx="5" cy="5" r="4" fill="none" stroke="#2a8db3" stroke-width="1.4"/></svg>Due in 8 days<b style="color:var(--blue);margin-left:12px">$</b>$ 15</div>
    </div>
    <div class="similar-item">
      <div class="thumb abs" role="img" aria-label="Task poster photo" style="left:460px;top:859px;width:41px;height:35px"></div>
      <div class="name" style="top:862px">WRITE 5 ONLINE STORE REVIEWS AND 1 PROFILE IMAGE</div>
      <div class="meta" style="left:511px;top:880px"><svg viewBox="0 0 10 10"><path d="M5 0a3.5 3.5 0 0 0-3.5 3.5C1.5 6 5 10 5 10s3.5-4 3.5-6.5A3.5 3.5 0 0 0 5 0z" fill="#2a8db3"/></svg>Online/Phone<svg viewBox="0 0 10 10" style="margin-left:8px"><circle cx="5" cy="5" r="4" fill="none" stroke="#2a8db3" stroke-width="1.4"/></svg>Due in 8 days<b style="color:var(--blue);margin-left:12px">$</b>$ 15</div>
    </div>
  </section>
</main>

<footer class="site-footer"></footer>
<a class="foot-link" style="left:183px">BROWSE TASKS</a>
<span class="foot-sep" style="left:261px"></span>
<a class="foot-link" style="left:285px">BECOME A RUNNER</a>
<span class="foot-sep" style="left:380px"></span>
<a class="foot-link" style="left:405px">POST A TASK</a>
<span class="foot-sep" style="left:475px"></span>
<a class="foot-link" style="left:500px">HOW IT WORKS</a>
<div class="foot-legal" style="left:183px">©&nbsp; 2013 &nbsp;TASKPERCH &nbsp;|&nbsp;&nbsp; PRIVACY POLICY &nbsp;&nbsp;|&nbsp;&nbsp; TERMS &amp; CONDITIONS</div>
<div class="friend-box">
  <div class="smile" role="img" aria-label="Smiley illustration"></div>
  <h3>TELL A FRIEND</h3>
  <p>AND GET $10 OFF!</p>
  <a class="invite">INVITE FRIENDS NOW »</a>
</div>
<span class="social" style="left:898px"></span>
<span class="social" style="left:928px"></span>
<span class="social" style="left:959px"></span>
<span class="social" style="left:990px"></span>

</body>
</html>
```